Concert Poster

Dear all!
It seems that we have found our final design!
Thanks a lot for your contribution so far. It is not necessary to post any more designs.

BR Jonas

____________________
For the band Velvet Groove - we would like to have a standard concert announcement poster that we can use to advertise for our gigs.The band plays the classic songs of the disco era end of the 70ies, e.g. Lusk, Vera Castell, Stone Rain & Ash, Brisk & The Crew etc. On stage we also adapt to the fashion of those times, but in a modern manner.See more details on our website: www.velvetgroove-band.de

We intend to position the band in the high price segment - so that poster should be positively effective even between posters of famous bands.

Format: DIN-A1 Portrait - 594 x 841 mm

If possible, it would also be great if we could use the same design to print flyers (format DIN-A6).

Target Market(s)

Live Music Bands

Requirements
Must have
• The poster should contain:
• - Our logo (see uploads)
• - Our official photo (see uploads)
• - Text about date, venue, time, entrance fee or the concert AND
• alternatively a possibility to leave this space blank so that we can print a bunch of empty posters that we can write the details on manually (to avoid printing posters for each gig individually)
• - Information about the Band:
• - Website: www.velvetgroove-band.de
• - Like us on facebook: fb/velvetgroovebavaria

```html
<!DOCTYPE html>
<html lang="en">
<head>
<meta charset="utf-8">
<title>Velvet Groove – Concert Poster</title>
<link href="https://fonts.googleapis.com/css2?family=Montserrat:wght@300;400;600;700&display=swap" rel="stylesheet">
<style>
  :root {
    --stage: #e9e9ec;
    --ink: #ffffff;
    --gold: #f4c948;
    --muted: #d6dbe4;
    --night-deep: #05080f;
    --blue-top: #1f5fa8;
    --blue-glow: #3fc6e8;
    --green-top: #3c8a2a;
    --green-glow: #d8e34a;
  }
  * { margin: 0; padding: 0; box-sizing: border-box; }
  html, body { width: 1200px; height: 800px; overflow: hidden; }
  body {
    background: var(--stage);
    font-family: "Montserrat", sans-serif;
    display: flex;
    justify-content: center;
    align-items: center;
    gap: 60px;
  }
  .poster {
    position: relative;
    width: 480px;
    height: 680px;
    overflow: hidden;
    color: var(--ink);
    background: var(--night-deep);
  }
  .poster--blue { --top: var(--blue-top); --glow: var(--blue-glow); }
  .poster--green { --top: var(--green-top); --glow: var(--green-glow); }
  .poster__backdrop {
    position: absolute; inset: 0;
    background:
      radial-gradient(ellipse 70% 40% at 50% 58%, color-mix(in srgb, var(--glow) 35%, transparent), transparent 70%),
      linear-gradient(180deg, var(--top) 0%, #0b1424 48%, var(--night-deep) 78%);
  }
  .poster--green .poster__backdrop {
    background:
      radial-gradient(ellipse 75% 45% at 50% 60%, color-mix(in srgb, var(--glow) 55%, transparent), transparent 72%),
      linear-gradient(180deg, var(--top) 0%, #4d6a1a 50%, #1a1a08 85%);
  }
  .band-photo {
    position: absolute; left: 20px; right: 20px; top: 20px; height: 300px;
    background:
      linear-gradient(180deg, transparent 60%, rgba(5,8,15,0.7) 100%),
      linear-gradient(100deg, #2a2f3c 0%, #8c6e4e 35%, #c9a06a 55%, #6b4d38 80%, #2a2f3c 100%);
    border-radius: 4px;
  }
  .logo {
    position: absolute; left: 0; right: 0; top: 210px;
    display: flex; flex-direction: column; align-items: center;
  }
  .logo__disc {
    width: 120px; height: 120px; border-radius: 50%;
    background: radial-gradient(circle at 40% 35%, #3d7fc4, #163a6e 70%);
    border: 2px solid color-mix(in srgb, var(--glow) 70%, white);
  }
  .logo__name {
    margin-top: 20px;
    font-weight: 700; font-size: 52px; line-height: 1.05;
    letter-spacing: 3px; text-align: center; text-transform: uppercase;
    color: var(--gold);
  }
  .event {
    position: absolute; left: 0; right: 0; top: 520px;
    display: flex; flex-direction: column; align-items: center;
  }
  .event__date { font-weight: 300; font-size: 34px; letter-spacing: 1px; }
  .event__details {
    margin-top: 22px; width: 330px;
    display: flex; justify-content: space-between; align-items: center;
    font-size: 11px; font-weight: 400;
  }
  .event__venue { font-weight: 600; font-size: 22px; }
  .links {
    position: absolute; left: 70px; right: 70px; bottom: 26px;
    display: flex; justify-content: space-between;
    font-size: 10px; color: var(--muted);
  }
</style>
</head>
<body>
  <article class="poster poster--blue">
    <div class="poster__backdrop"></div>
    <div class="band-photo" role="img" aria-label="Official band photo: seven band members in disco-era outfits on a lit stage"></div>
    <div class="logo">
      <div class="logo__disc"></div>
      <div class="logo__name">Velvet<br>Groove</div>
    </div>
    <section class="event">
      <p class="event__date">25 DECEMBER 2018</p>
      <div class="event__details">
        <span>starts at 22:00</span>
        <span class="event__venue">Marlowe Club</span>
        <span>entrance 10$</span>
      </div>
    </section>
    <footer class="links">
      <span>www.velvetgroove-band.de</span>
      <span>facebook.com/velvetgroovebavaria</span>
    </footer>
  </article>

  <article class="poster poster--green">
    <div class="poster__backdrop"></div>
    <div class="band-photo" role="img" aria-label="Official band photo: seven band members in disco-era outfits on a lit stage"></div>
    <div class="logo">
      <div class="logo__disc"></div>
      <div class="logo__name">Velvet<br>Groove</div>
    </div>
    <section class="event">
      <p class="event__date">25 DECEMBER 2018</p>
      <div class="event__details">
        <span>starts at 22:00</span>
        <span class="event__venue">Marlowe Club</span>
        <span>entrance 10$</span>
      </div>
    </section>
    <footer class="links">
      <span>www.velvetgroove-band.de</span>
      <span>facebook.com/velvetgroovebavaria</span>
    </footer>
  </article>
</body>
</html>
```